Brochure Design Project for Brockwell and Daughter Lumber

We are after an executive high-end trifold brochure to be sent to new customers. Please refer to document attached ('brochure notes') for the details.

Target Market(s)

Renovators, Wives, Architects, Builders

Requirements
Must have
• Back of brochure must have a map and contact details.

Must relate to the feel of our website ... brockwellanddaughterlumber.net

Nice to have
• A unique design - something unlike regular brochures.

Developed using Adobe Photoshop or InDesign

```html
<!DOCTYPE html>
<html lang="en">
<head>
<meta charset="utf-8">
<title>Brockwell and Daughter Lumber – Trifold Brochure</title>
<link rel="stylesheet" href="https://fonts.googleapis.com/css2?family=Josefin+Slab:wght@400;600&family=Open+Sans:wght@400;600;700&display=swap">
<style>
  :root{
    --page:#ffffff;
    --bark:#36302a;
    --sand:#e3ddcc;
    --leaf:#79b443;
    --forest-a:#2f5a24;
    --forest-b:#5f9a3a;
    --forest-c:#9cc86a;
    --ink:#2a2622;
  }
  *{box-sizing:border-box;margin:0;padding:0}
  html,body{width:847px;height:1200px;overflow:hidden;background:var(--page)}
  body{position:relative;font-family:"Open Sans",Arial,sans-serif;color:var(--ink)}
  .abs{position:absolute}
  .slab{font-family:"Josefin Slab",Georgia,serif}

  /* ---------- outside spread ---------- */
  .outside{left:17px;top:17px;width:813px;height:574px;background:var(--bark)}
  .forest{left:0;top:0;width:813px;height:419px;
    background:linear-gradient(160deg,var(--forest-c) 0%,var(--forest-b) 35%,var(--forest-a) 75%,#24401b 100%)}
  .forest-shade{left:0;top:0;width:271px;height:419px;background:rgba(30,34,26,.62)}
  .offer{left:34px;top:28px;width:225px;color:#fff}
  .offer h3{font-weight:400;font-size:15px;line-height:1.2}
  .offer p.small{font-family:"Open Sans",Arial,sans-serif;font-size:10.5px;line-height:1.35;margin-bottom:14px}
  .offer p.item{font-size:14px;line-height:1.25;margin-bottom:13px}
  .contact{left:305px;top:310px;color:#e9eee2;font-size:9.5px;line-height:1.3}
  .contact table{border-collapse:collapse;margin-top:10px}
  .contact td{padding:0 4px 0 0;vertical-align:top}
  .intro{left:560px;top:306px;width:250px;text-align:center;color:#fff;font-weight:600;font-size:12.5px;line-height:1.35;text-shadow:0 1px 2px rgba(0,0,0,.5)}
  .question{left:30px;top:450px;width:200px;text-align:center;color:#fff;font-size:15px;line-height:1.2}
  .question .big{font-size:22px}
  .map{left:318px;top:429px;width:177px;height:136px;background:linear-gradient(135deg,#e8e6de,#d6dccb);border:3px solid #cfcac0}
  .brand-panel{left:560px;top:440px;width:230px;height:120px;display:flex;flex-direction:column;align-items:center;justify-content:center;gap:10px}
  .brand-name{font-family:"Open Sans",Arial,sans-serif;font-weight:700;font-size:17px;color:var(--leaf);text-align:center;line-height:1.15}

  /* ---------- inside spread ---------- */
  .inside{left:17px;top:608px;width:813px;height:574px;background:var(--bark)}
  .about-col{left:0;top:0;width:270px;height:510px;background:linear-gradient(180deg,#dcdcdc,#f0f0f0 60%,#f6f6f6)}
  .about{left:32px;top:18px;width:230px;font-size:10.5px;line-height:1.38;font-weight:600;color:#3a3530;text-align:justify}
  .about h2{font-size:12px;font-weight:700;color:#2b2621}
  .about p+p{margin-top:14px}
  .couple{left:0;top:279px;width:270px;height:231px;background:linear-gradient(150deg,#cfc9bd,#a79b88 55%,#8e7f6b)}
  .row{left:270px;width:543px;height:127px;overflow:hidden}
  .row.dark{background:var(--bark)}
  .row.light{background:var(--sand)}
  .row .txt{position:absolute;left:4px;top:10px;width:271px;text-align:center;font-size:9px;line-height:1.3}
  .row.dark .txt{color:#ece6da}
  .row.light .txt{color:#2b2621}
  .row h3{font-family:"Josefin Slab",Georgia,serif;font-weight:600;font-size:13px;letter-spacing:.3px;margin-bottom:3px;line-height:1.1}
  .row .gap{display:block;height:7px}
  .row .photo{position:absolute;left:283px;top:8px;width:252px;height:110px}
  .p-deck{background:linear-gradient(135deg,#4f7a3c,#b47c5a 55%,#c48a66)}
  .p-boards{background:linear-gradient(120deg,#6e2c14,#a94f24 45%,#7b351a)}
  .p-fence{background:linear-gradient(100deg,#b86a48,#c98560 50%,#8c8f92)}
  .p-floor{background:linear-gradient(180deg,#dcdad4,#c9b48c 60%,#a7834c)}
  .foot{left:0;top:510px;width:813px;height:64px;background:var(--bark);display:flex;align-items:center;justify-content:center;gap:10px;padding-left:20px}
  .foot .brand-name{font-size:15px}
</style>
</head>
<body>

<section class="abs outside">
  <div class="abs forest" role="img" aria-label="Photo of a lush green forest with tall tree trunks"></div>
  <div class="abs forest-shade"></div>

  <div class="abs offer slab">
    <h3>Want Cash?</h3>
    <p class="small">Become a renovation star!<br>If you allow us to take photos, video or leave a sign, we will reward you with $50 cash for every order taken from interest in your home improvement.</p>
    <p class="item">We can come to you for free measure and quote.</p>
    <p class="item">Design advise</p>
    <p class="item">Can organize full installation</p>
    <p class="item">Feel free to use any info or pictures from our website</p>
  </div>

  <div class="abs contact">
    Unit 7 / 22 Ridgeline Road<br>HOLLOWAY PARK 4230
    <table>
      <tr><td>Call</td><td>: 1300 555 014 | (07) 5550 1482</td></tr>
      <tr><td>Fax</td><td>: (07) 5550 1483</td></tr>
      <tr><td>Email</td><td>: info@brockwellanddaughterlumber.com.au</td></tr>
      <tr><td>Web</td><td>: http://brockwellanddaughterlumber.net</td></tr>
    </table>
  </div>

  <p class="abs intro">We are modern timber suppliers specializing in decks, hardwood floors and external cladding.<br>We provide high end service to builders, DIY and tradesmen.</p>

  <p class="abs question slab">Looking for something<br><span class="big">different</span><br>or<br><span class="big">unique?</span></p>

  <div class="abs map" role="img" aria-label="Street map showing the showroom location"></div>

  <div class="abs brand-panel">
    <svg width="40" height="40" viewBox="0 0 40 40" aria-hidden="true"><circle cx="20" cy="20" r="19" fill="var(--leaf)"/></svg>
    <div class="brand-name">Brockwell &amp; Daughter<br>Lumber</div>
  </div>
</section>

<section class="abs inside">
  <div class="abs about-col"></div>
  <div class="abs about">
    <h2>About Us</h2>
    <p>Welcome to Brockwell and Daughter Lumber, from the family that brought you Stonegrain Timbers. We understand that deciding on the perfect project for home comes with lots of questions. We’re the experts not only in timber, but design, engineering and construction. Be it a little fence or the largest house, our friendly team is here to help.</p>
    <p>We invite you to take your time looking over our website. We hope you find some inspiration to create your own masterpiece at your place. Don’t forget we’re only a phone call away and we’re more than happy to assist.</p>
  </div>
  <div class="abs couple" role="img" aria-label="Photo of a smiling couple planning a renovation over floor plans"></div>

  <div class="abs row dark" style="top:0">
    <div class="txt" style="top:14px">
      <h3>COMPOSITE TIMBER</h3>
      Timber decks and screening are very popular but require constant maintenance. This timber-like product gives the look of timber, but with minimal upkeep. .
      <span class="gap"></span>
      The ‘greenest of green’ ... This timber-like product will give you the look you’re after, without needing to oil .... EVER!
    </div>
    <div class="photo p-deck" role="img" aria-label="Photo of a composite timber deck beside a pool"></div>
  </div>

  <div class="abs row light" style="top:127px">
    <div class="txt" style="top:8px">
      <h3>RIDGEBACK TIMBER</h3>
      The products include decking, flooring,<br>structural timber and step treads.
      <span class="gap"></span>
      <b>Benefits of the Ridgeback Timber species:</b><br>
      Durability Class 1 – no need to treat with nasty chemicals<br>
      Environmentally sustainable – fully certified<br>
      Strong | Beautiful<br>
      Wide range of uses available – decking, step treads,<br>posts, joists.
    </div>
    <div class="photo p-boards" role="img" aria-label="Photo of rich red hardwood decking boards"></div>
  </div>

  <div class="abs row dark" style="top:254px">
    <div class="txt" style="top:30px">
      <h3>FEATURE FENCING</h3>
      We are able to supply you with designer fencing fully<br>installed for much less<br>than you think. Endless combinations available.<br>Call for an obligation-free quote today.
    </div>
    <div class="photo p-fence" role="img" aria-label="Photo of a slatted timber feature fence"></div>
  </div>

  <div class="abs row light" style="top:381px">
    <div class="txt" style="top:12px">
      <h3>TRADITIONAL TIMBER AND<br>BAMBOO FLOORING</h3>
      Bamboo flooring is becoming an increasingly popular choice for many homeowners, architects, builders and interior designers who are looking for an environmental alternative<br>to timber flooring that is a stylish,<br>hard wearing, pre-finished flooring system.
    </div>
    <div class="photo p-floor" role="img" aria-label="Photo of a polished bamboo floor in a bright room"></div>
  </div>

  <div class="abs foot">
    <svg width="30" height="30" viewBox="0 0 30 30" aria-hidden="true"><circle cx="15" cy="15" r="14" fill="var(--leaf)"/></svg>
    <div class="brand-name">Brockwell &amp; Daughter Lumber</div>
  </div>
</section>

</body>
</html>
```